Business Consulting Company requires a website design (PSD+HTML+CSS required)

Tarnvale Advisory is a Business Consulting Company that provides Analysis, Business Coaching and Systems and Document Design for clients.

We would like a simplistic yet professional looking website design that uses high quality imagery to project a professional persona across our entire site.

The completed project will need to include PSD files (for editing in Photoshop) and will need to also include HTML+CSS coded files that can be edited in Adobe Dreamweaver CS5.5.

Tarnvale Advisory currently has a functioning website (located at www.tarnvaleadvisory.com.au) but would like to replace its current site with something more professional, user friendly and content simplistic, with the overall design of this project being clean and very easy to navigate whilst remaining professionally focused.

A brief has been attached to this project to provide the key details but please feel free to contact me if you require any clarification or have any questions regarding the project.

Target Market(s)

The target audience for this website will be small to medium sized businesses (of all descriptions).

Industry/Entity Type

Business

Coding

Coded - Design and coding required

Number of Pages Required

5+ page

Requirements
Must have
• Simplistic design structure
• Professional images
• Easy to navigate
• Must be uploaded in PSD format
• Must be coded (HTML+CSS) and compatible with Adobe Dreamweaver CS5.5
Nice to have
• Use of the Company’s corporate colours throughout the site design
• Adding a Home page slider bar with images and short catchy messages (i.e. text based statements)
• Having a quick link box on each page that provides easy navigation throughout the site
• The use of different icons and images to depict our different services (i.e. a different icon and image for analysis service and coaching service etc.).
• All pages should follow a similar theme (universal approach to all pages)
Should not have
• When coding, images should not be used in place of text (all text must be editable)

```html
<!DOCTYPE html>
<html lang="en">
<head>
<meta charset="utf-8">
<title>Tarnvale Advisory</title>
<link href="https://fonts.googleapis.com/css2?family=Titillium+Web:wght@400;600&family=Open+Sans:wght@400&family=Arimo:ital,wght@0,400;1,400&display=swap" rel="stylesheet">
<style>
:root{
  --blue:#3a8fd9;
  --band:#3f95d9;
  --band-dark:#3484c8;
  --ink:#3d3d3d;
  --muted:#707070;
  --line:#dcdcdc;
  --hero:#e4e4e4;
  --footer:#111111;
  --white:#ffffff;
}
*{margin:0;padding:0;box-sizing:border-box}
html,body{width:932px;height:1200px;overflow:hidden;background:var(--white)}
body{position:relative;font-family:"Arimo",Arial,sans-serif;color:var(--ink)}
.abs{position:absolute}
.topline{left:0;top:0;width:932px;height:2px;background:var(--blue)}
.brand{left:102px;top:34px;display:flex;align-items:center;gap:10px}
.brand-dot{width:30px;height:30px;border-radius:50%;background:var(--blue)}
.brand-name{font-family:"Titillium Web",sans-serif;font-weight:400;font-size:25px;color:#555;letter-spacing:1px}
.phone{left:724px;top:13px;display:flex;align-items:center;gap:8px;font-family:"Open Sans",sans-serif;font-size:12px;color:#444}
.nav{top:56px;left:0;width:932px;font-family:"Open Sans",sans-serif;font-size:10.5px;color:#333}
.nav span{position:absolute;white-space:nowrap}
.nav .active{color:var(--blue)}
.hero{left:0;top:102px;width:932px;height:405px;background:var(--hero)}
.hero-photo{position:absolute;left:340px;top:0;width:592px;height:405px;background:linear-gradient(100deg,#ececec 0%,#f6f6f6 30%,#b9c2cc 55%,#5a5a60 80%,#8a96a6 100%)}
.hero-title{position:absolute;left:82px;top:128px;font-family:"Titillium Web",sans-serif;font-weight:600;font-size:36px;line-height:51px;color:#3a3a3a;letter-spacing:1px}
.hero-title .accent{color:var(--blue)}
.arrow{position:absolute;top:183px}
.section-title{font-family:"Titillium Web",sans-serif;font-weight:600;font-size:20px;color:#444}
.section-title .accent{color:var(--blue)}
.card{top:604px;width:174px;height:295px;border:1px solid var(--line);background:var(--white)}
.card-icon{position:absolute;left:58px;top:-30px;width:58px;height:58px;border-radius:50%;background:var(--white);border:1px solid var(--line);display:flex;align-items:center;justify-content:center}
.card-photo{position:absolute;left:12px;top:38px;width:150px;height:107px;border:2px solid #f2f2f2;box-shadow:0 3px 4px rgba(0,0,0,.15)}
.card h3{position:absolute;left:10px;top:160px;width:160px;font-family:"Titillium Web",sans-serif;font-weight:600;font-size:13px;line-height:17.5px;color:var(--blue)}
.card p{position:absolute;left:10px;width:156px;font-size:8.6px;line-height:18.4px;color:var(--muted);text-align:justify}
.band{left:0;top:930px;width:932px;height:210px;background:var(--band);color:var(--white)}
.band h2{position:absolute;font-family:"Titillium Web",sans-serif;font-weight:600;font-size:19px;letter-spacing:.3px}
.welcome-text{position:absolute;left:102px;top:68px;width:446px;font-size:8.6px;line-height:17.6px}
.welcome-text p+p{margin-top:10px}
.quote{position:absolute;left:578px;top:67px;width:252px;height:93px;background:var(--band-dark);padding:14px 15px 0 32px;font-size:8.6px;line-height:17.6px;text-align:justify}
.quote-mark{position:absolute;left:13px;top:6px;font-family:"Titillium Web",sans-serif;font-size:24px;font-weight:600}
.quote-tail{position:absolute;left:50px;bottom:-7px;width:0;height:0;border-left:6px solid transparent;border-right:6px solid transparent;border-top:7px solid var(--band-dark)}
.quote-name{position:absolute;left:618px;top:177px;font-style:italic;font-size:9px}
.footer{left:0;top:1140px;width:932px;height:60px;background:var(--footer)}
.copyright{position:absolute;left:104px;top:22px;font-size:9.5px;color:#cfcfcf}
.social{position:absolute;top:18px;width:25px;height:25px;border-radius:50%;border:1px solid #9a9a9a}
</style>
</head>
<body>
<div class="abs topline"></div>

<header>
  <div class="abs brand"><div class="brand-dot"></div><span class="brand-name">Tarnvale Advisory</span></div>
  <div class="abs phone">
    <svg width="20" height="20" viewBox="0 0 20 20"><circle cx="10" cy="10" r="9" fill="none" stroke="#3a8fd9" stroke-width="1.3"/><path d="M7 5.5l1.8 2.2-1 1.2a6 6 0 0 0 3.3 3.3l1.2-1 2.2 1.8-1 1.6c-3.8-.3-6.8-3.3-7.1-7.1z" fill="#3a8fd9"/></svg>
    <span>0352 418 907</span>
  </div>
  <nav class="abs nav">
    <span class="active" style="left:458px">HOME</span>
    <span style="left:518px">ABOUT US</span>
    <span style="left:597px">SERVICES</span>
    <span style="left:670px">CONTACT US</span>
    <span style="left:760px">TESTIMONIALS</span>
  </nav>
</header>

<section class="abs hero">
  <div class="hero-photo" role="img" aria-label="Photo of a consultant presenting a chart on a flip board to a seated team"></div>
  <h1 class="hero-title">EXPERT ADVICE<br>AT YOUR<br><span class="accent">FINGERTIPS</span></h1>
  <svg class="arrow" style="left:26px" width="16" height="34" viewBox="0 0 16 34"><path d="M14 2L2 17l12 15" fill="none" stroke="#fff" stroke-width="1.5"/></svg>
  <svg class="arrow" style="left:888px" width="16" height="34" viewBox="0 0 16 34"><path d="M2 2l12 15L2 32" fill="none" stroke="#fff" stroke-width="1.5"/></svg>
</section>

<section>
  <svg class="abs" style="left:102px;top:528px" width="26" height="26" viewBox="0 0 26 26"><circle cx="10" cy="15" r="7" fill="none" stroke="#c8c8c8" stroke-width="4" stroke-dasharray="3 2"/><circle cx="19" cy="7" r="4" fill="none" stroke="#c8c8c8" stroke-width="3" stroke-dasharray="2 1.5"/></svg>
  <h2 class="abs section-title" style="left:138px;top:530px">OUR <span class="accent">SERVICES</span></h2>

  <article class="abs card" style="left:102px">
    <div class="card-icon"><svg width="42" height="42" viewBox="0 0 42 42"><circle cx="21" cy="21" r="19" fill="none" stroke="#3a8fd9" stroke-width="2.5" stroke-dasharray="26 4"/><rect x="13" y="19" width="3" height="8" fill="#3a8fd9"/><rect x="18" y="14" width="3" height="13" fill="#3a8fd9"/><circle cx="25" cy="22" r="3" fill="none" stroke="#3a8fd9" stroke-width="2"/><path d="M27 24l3 3" stroke="#3a8fd9" stroke-width="2"/></svg></div>
    <div class="card-photo" role="img" aria-label="Photo of colleagues discussing documents at a meeting table" style="background:linear-gradient(135deg,#d9dde3,#8a8f98 60%,#4a4f58)"></div>
    <h3>BUSINESS ANALYSIS</h3>
    <p style="top:183px">Pinpoint critical goals and objectives to bring about maximum profitability and productivity through Tarnvale's in depth and comprehensive business analysis reports.</p>
  </article>

  <article class="abs card" style="left:287px">
    <div class="card-icon"><svg width="42" height="42" viewBox="0 0 42 42"><circle cx="21" cy="21" r="19" fill="none" stroke="#3a8fd9" stroke-width="2.5" stroke-dasharray="26 4"/><path d="M10 19l5-4 6 3 6-3 5 4-6 7h-4z" fill="#3a8fd9"/></svg></div>
    <div class="card-photo" role="img" aria-label="Photo of a coach presenting to a seated group" style="background:linear-gradient(135deg,#e6ebf0,#b9c6d3 55%,#7e8fa3)"></div>
    <h3>BUSINESS COACHING</h3>
    <p style="top:183px">Transfer essential business knowledge into your business, Brainstorm new and existing concepts, or develop and implement specific strategies via Tarnvale's one...</p>
  </article>

  <article class="abs card" style="left:472px">
    <div class="card-icon"><svg width="42" height="42" viewBox="0 0 42 42"><circle cx="21" cy="21" r="19" fill="none" stroke="#3a8fd9" stroke-width="2.5" stroke-dasharray="26 4"/><path d="M15 12h9l4 4v14H15z" fill="none" stroke="#3a8fd9" stroke-width="1.8"/><path d="M18 19h7M18 22h7M18 25h7" stroke="#3a8fd9" stroke-width="1.4"/></svg></div>
    <div class="card-photo" role="img" aria-label="Photo of a smiling businesswoman at her desk" style="background:linear-gradient(135deg,#c9b7a6,#e8ddd4 50%,#9aa0a8)"></div>
    <h3>BUSINESS SYSTEM DESIGN AND DOCUMENT</h3>
    <p style="top:201px">Save time, money and free up valuable resources by outsourcing your business system or document creation projects to us.</p>
  </article>

  <article class="abs card" style="left:657px">
    <div class="card-icon"><svg width="42" height="42" viewBox="0 0 42 42"><circle cx="21" cy="21" r="19" fill="none" stroke="#3a8fd9" stroke-width="2.5" stroke-dasharray="26 4"/><path d="M28 13c-6 0-10 4-12 10l3 3c6-2 10-6 10-12z" fill="none" stroke="#3a8fd9" stroke-width="1.8"/><path d="M15 28l2-4M14 25l-2 1" stroke="#3a8fd9" stroke-width="1.6"/></svg></div>
    <div class="card-photo" role="img" aria-label="Photo of a team meeting around a boardroom table" style="background:linear-gradient(135deg,#dfe5ea,#a7b3bf 55%,#5c6670)"></div>
    <h3>NEW BUSINESS START-UP PACKAGES</h3>
    <p style="top:201px">Starting a new business? Tarnvale provides simplistic, hassle free and easy to administer start-up packages that are a perfect...</p>
  </article>
</section>

<section class="abs band">
  <svg class="abs" style="left:102px;top:34px" width="20" height="18" viewBox="0 0 20 18"><path d="M10 1L1 9h3v8h12V9h3z" fill="#5aa6e2"/></svg>
  <h2 style="left:131px;top:21px">WELCOME TO TARNVALE ADVISORY</h2>
  <div class="welcome-text">
    <p>Tarnvale Advisory is a business analysis, coaching and business development provider who specialises in assisting businesses to achieve maximum efficiency, increased productivity and who can assist with improving a business's overall profitability.</p>
    <p>At Tarnvale, we pride ourselves on our ability to form strong client relationships whilst delivering impressive results. For us, it's all about effective communication coupled with practical and measurable results!</p>
  </div>

  <svg class="abs" style="left:576px;top:34px" width="20" height="18" viewBox="0 0 20 18"><rect x="1" y="1" width="12" height="9" fill="#5aa6e2"/><rect x="6" y="6" width="13" height="9" fill="#5aa6e2"/></svg>
  <h2 style="left:606px;top:21px">OUR TESTIMONIALS</h2>
  <svg class="abs" style="left:808px;top:34px" width="18" height="14" viewBox="0 0 18 14"><path d="M7 2L2 7l5 5" fill="none" stroke="#fff" stroke-width="1.6"/><path d="M11 2l5 5-5 5" fill="none" stroke="#7fb8e8" stroke-width="1.6"/></svg>

  <div class="quote">
    <span class="quote-mark">“</span>
    We envisage a simplistic design on this page with possibly a single image accompanied by some text that we can separate to depict the testimonials from each client We envisage
    <span class="quote-tail"></span>
  </div>
  <div class="quote-name">Dana Whitlock</div>
</section>

<footer class="abs footer">
  <div class="copyright">© Copy Rights 2014 - Tarnvale Advisory . All rights reserved</div>
  <span class="social" style="left:719px"></span>
  <span class="social" style="left:754px"></span>
  <span class="social" style="left:793px"></span>
</footer>
</body>
</html>
```